real esate business card with company logo and name

we need a business card design for a real esate company

The company name is Walsh & Brody Pty Ltd, and we have our logo designed and will upload. We want classic or moden feel. Black or white background. looks more textured. Should include folowinginformations
Paul Walsh and Lucy Brody
Sales Agents & Onsite Manager
p: 07 5948 2063
F: 07 5948 2174
M:0461 857 239
3/42 Marlin Crescent, ELLEN GROVE QLD 4078

We want this business card looks professonal. Thank you in advance.

Industry/Entity Type

Real Estate Agent

Contact Information for Business Card

Paul Walsh and Lucy Brody
Onsite Manager & Sales Agents
p: 07 5948 2063
M:0461 857 239

Font styles to use
Serif

Colors
000000
fbfbfb
333333
959595

Requirements
Must have
• company logo and name, black or white back ground

```html
<!DOCTYPE html>
<html lang="en">
<head>
<meta charset="utf-8">
<title>Walsh &amp; Brody Pty Ltd — Business Card</title>
<link rel="stylesheet" href="https://fonts.googleapis.com/css2?family=Alegreya+Sans:wght@700&family=Open+Sans:wght@700&display=swap">
<style>
  :root {
    --black: #000000;
    --near-white: #fbfbfb;
    --charcoal: #333333;
    --mid-grey: #959595;
    --label-grey: #585858;
    --subtitle-grey: #4a4a4a;
    --band-edge: #0b0f18;
  }
  html, body {
    margin: 0;
    padding: 0;
    width: 1200px;
    height: 686px;
    overflow: hidden;
    background: var(--black);
  }
  .card {
    position: relative;
    width: 1200px;
    height: 686px;
    overflow: hidden;
    background:
      radial-gradient(ellipse 720px 620px at 980px 200px, #3d3d3d 0%, #262626 45%, rgba(0,0,0,0) 100%),
      linear-gradient(90deg, var(--black) 0%, var(--black) 40%, #1a1a1a 70%, #2a2a2a 100%);
    font-family: "Alegreya Sans", sans-serif;
    font-variant-numeric: lining-nums;
    color: var(--near-white);
  }
  .brand-mark {
    position: absolute;
    left: 150px;
    top: 110px;
    width: 260px;
    height: 260px;
    background: var(--mid-grey);
  }
  .brand-band {
    position: absolute;
    left: 0;
    top: 417px;
    width: 564px;
    height: 76px;
    background: var(--band-edge);
    border-radius: 0 4px 4px 0;
  }
  .brand-name {
    position: absolute;
    left: 0;
    top: 437px;
    width: 544px;
    height: 38px;
    margin: 0;
    background: var(--near-white);
    text-align: center;
    font-family: "Alegreya Sans", sans-serif;
    font-weight: 700;
    font-size: 31px;
    line-height: 38px;
    letter-spacing: 2px;
    color: var(--charcoal);
    white-space: nowrap;
    padding-left: 36px;
    box-sizing: border-box;
  }
  .people {
    position: absolute;
    left: 560px;
    top: 86px;
    width: 620px;
    text-align: center;
  }
  .people-names {
    margin: 0;
    font-size: 46px;
    font-weight: 700;
    line-height: 1;
    letter-spacing: 0.5px;
    color: var(--near-white);
    white-space: nowrap;
  }
  .people-roles {
    margin: 4px 0 0 0;
    font-family: "Open Sans", sans-serif;
    font-weight: 700;
    font-size: 26px;
    line-height: 1.1;
    letter-spacing: 1.5px;
    color: var(--subtitle-grey);
    white-space: nowrap;
  }
  .contact {
    position: absolute;
    right: 66px;
    top: 420px;
    margin: 0;
    padding: 0;
    list-style: none;
    text-align: right;
    font-size: 40px;
    font-weight: 700;
    line-height: 51px;
    letter-spacing: 1px;
  }
  .contact li { white-space: nowrap; }
  .contact-label {
    color: var(--label-grey);
    margin-right: 20px;
  }
  .contact-label--address { margin-right: 8px; }
</style>
</head>
<body>
  <main class="card">
    <section class="brand">
      <div class="brand-mark" aria-hidden="true"></div>
      <div class="brand-band" aria-hidden="true"></div>
      <p class="brand-name">WALSH &amp; BRODY PTY LTD</p>
    </section>

    <header class="people">
      <h1 class="people-names">Paul Walsh and Lucy Brody</h1>
      <p class="people-roles">Onsite Manager &amp; Sales Agents</p>
    </header>

    <ul class="contact">
      <li><span class="contact-label">P</span>07 5948 2063</li>
      <li><span class="contact-label">M</span>0461 857 239</li>
      <li><span class="contact-label contact-label--address">A</span>3/42 Marlin Crescent</li>
      <li>HARLOW PARK QLD 4517</li>
    </ul>
  </main>
</body>
</html>
```